Real Estate stationery - need an interesting, eye catching design

I need a letterhead and #10 envelope design in the same theme.
I am looking for an interesting, eye catching design that would stand out in the crowd. I am in the real estate business(which is very competitive) in Florida so standing out and being different is very important to me.
Marguerite(Dee) Calloway (name), RealtorĀ® (title), 407-555-0263 (cell), sunbeltdeehomes@quillpost.net (email), www.sunbeltdeehomes.net(website), 915 Harrow Creek Blvd.,Ste. 3170, Longwood, FL 32766 (business address)
Industry/Entity Type
Real Estate Agent
Colors
Designer to choose colors to be used in the design.
Look and feel

```html
<!DOCTYPE html>
<html lang="en">
<head>
<meta charset="utf-8">
<title>Harborline Realty Stationery</title>
<link href="https://fonts.googleapis.com/css2?family=Roboto:wght@400;500&display=swap" rel="stylesheet">
<style>
  :root {
    --backdrop: #d9d9d9;
    --paper: #efefef;
    --flap: #f4f4f4;
    --brown: #875d27;
    --grey: #8a8b8e;
    --ink: #4a4a4a;
    --white: #ffffff;
  }
  * { margin: 0; padding: 0; box-sizing: border-box; }
  html, body { width: 1200px; height: 947px; overflow: hidden; }
  body {
    background: var(--backdrop);
    font-family: 'Roboto', Arial, sans-serif;
    color: var(--ink);
    position: relative;
  }
  .brand { display: flex; align-items: center; gap: 8px; }
  .brand-mark { width: 12px; height: 12px; background: var(--brown); flex: none; }
  .brand-name { font-size: 20px; font-weight: 500; color: var(--brown); white-space: nowrap; }

  .letterhead {
    position: absolute;
    left: 72px; top: 82px;
    width: 553px; height: 782px;
    background: var(--paper);
  }
  .letterhead .brand { position: absolute; left: 34px; top: 72px; }
  .contact {
    position: absolute;
    left: 386px; top: 58px;
    padding-left: 11px;
    border-left: 1px solid #b9b9b9;
    font-size: 6.8px; line-height: 8.4px;
  }
  .contact .address { margin-bottom: 4px; }
  .contact-row { display: flex; align-items: center; gap: 4px; }
  .contact-row svg { width: 6px; height: 6px; fill: var(--brown); }
  .footer-bands { position: absolute; left: 0; bottom: 0; width: 100%; display: block; }
  .website {
    position: absolute;
    right: 34px; bottom: 10px;
    font-size: 6.8px; letter-spacing: 0.8px;
    color: var(--white);
  }

  .envelope-back {
    position: absolute;
    left: 570px; top: 381px;
    width: 579px; height: 289px;
    background: var(--paper);
  }
  .envelope-flap { position: absolute; left: 0; top: 0; width: 579px; height: 88px; display: block; }
  .envelope-back .brand {
    position: absolute; left: 0; right: 0; top: 40px;
    justify-content: center; padding-left: 20px;
  }
  .envelope-back .brand-name { font-size: 16px; }
  .envelope-back .brand-mark { width: 10px; height: 10px; }

  .envelope-front {
    position: absolute;
    left: 475px; top: 532px;
    width: 634px; height: 290px;
    background: var(--paper);
    box-shadow: -1px 0 2px rgba(0,0,0,0.08);
  }
  .return-address {
    position: absolute;
    left: 29px; top: 48px;
    width: 132px;
    display: flex; flex-direction: column; align-items: center;
  }
  .return-address .brand-name { font-size: 16px; }
  .return-address .brand-mark { width: 10px; height: 10px; }
  .return-address p {
    margin-top: 22px;
    font-size: 6.8px; line-height: 8.4px; text-align: center; white-space: nowrap;
  }
</style>
</head>
<body>

<section class="letterhead">
  <div class="brand">
    <span class="brand-mark"></span>
    <span class="brand-name">Harborline Realty</span>
  </div>

  <div class="contact">
    <p class="address">915 Harrow Creek Blvd.,<br>Ste. 3170<br>Longwood, FL 32766</p>
    <div class="contact-row">
      <svg viewBox="0 0 6 6"><rect x="1.5" y="0" width="3" height="6" rx="0.6"/><rect x="2" y="0.8" width="2" height="3.6" fill="#efefef"/></svg>
      <span>407-555-0263</span>
    </div>
    <div class="contact-row">
      <svg viewBox="0 0 6 6"><rect x="0" y="1" width="6" height="4" rx="0.6"/></svg>
      <span>sunbeltdeehomes@quillpost.net</span>
    </div>
  </div>

  <svg class="footer-bands" viewBox="0 0 553 26" height="26" preserveAspectRatio="none">
    <polygon points="0,5 370,5 362,16 0,16" fill="#8a8b8e"/>
    <polygon points="0,18 359,18 378,2 553,2 553,26 0,26" fill="#875d27"/>
  </svg>
  <span class="website">www.sunbeltdeehomes.net</span>
</section>

<section class="envelope-back">
  <svg class="envelope-flap" viewBox="0 0 579 88">
    <path d="M0,0 L579,0 C573,30 569,55 565,66 C560,78 552,83 538,83 L40,83 C26,83 19,78 16,66 C12,52 6,28 0,0 Z"
          fill="#f5f5f5" stroke="#dcdcdc" stroke-width="1"/>
  </svg>
  <div class="brand">
    <span class="brand-mark"></span>
    <span class="brand-name">Harborline Realty</span>
  </div>
</section>

<section class="envelope-front">
  <div class="return-address">
    <div class="brand">
      <span class="brand-mark"></span>
      <span class="brand-name">Harborline Realty</span>
    </div>
    <p>915 Harrow Creek Blvd.,Ste. 3170<br>Longwood, FL 32766</p>
  </div>

  <svg class="footer-bands" viewBox="0 0 634 24" height="24" preserveAspectRatio="none">
    <polygon points="0,4 460,4 451,14 0,14" fill="#8a8b8e"/>
    <polygon points="0,17 447,17 466,0 634,0 634,24 0,24" fill="#875d27"/>
  </svg>
</section>

</body>
</html>
```